Dog care service needs advertising poster

Our company is Paw Haven. We provide care for dogs while their owners are away, either through home visits or a holiday stay in the homes of carefully selected minders. Our existing website & Facebook cover should provide all the colour cues for a poster - namely blues, blondes and grey. We have an existing logo (provided). We can feature the same imagery from our website as I have purchased the rights to the stock images.

www.pawhavenexample.com.au
www.facebook.com/pawhavenexampleau

This brief is for design of a poster that can be placed in vet surgeries, groomers, on community noticeboards. It should be scalable to print in three sizes, A5, A4 & A3.

We wish to clearly communicate our three areas of service "dog minding, home visits, dog walking".

We would like to have the files ready for upload to Printora (or similar) for immediate printing.

Target Market(s)

Dog owners who love their dogs like family.

Industry/Entity Type

Advertising

Font styles to use
Sans Serif

Colors
33a6d7
3276b5

Requirements
Must have
• Logo
• www.pawhavenexample.com.au
• Telephone number
• Three services - Dog Minding, Home Visits, Dog Walking
Nice to have
• use of our existing stock photography to highlight the three areas of service - Dog minding, home visits, dog walking. Existing colour palette - blues, blondes and grey.
• Text that can be used:
• Western Sydney’s complete dog care service.
• Dog Minding - Your dog stays in the home of one of our carefully selected minders.Treated like part of the family, they enjoy all the creature comforts they are used to.
• Home Visits - We visit your dog at your home for feeding, walking and playtime. Short of long visits available.
• Dog Walking - If you can't walk your dog for any reason we are here to help. 1/2 hour or hourly walks available.
• Contact us today for a tailored package to meet your needs.
Should not have
• Any additional illustrations beyond the logo.

```html
<!DOCTYPE html>
<html lang="en">
<head>
<meta charset="utf-8">
<title>Paw Haven – Poster Options</title>
<link href="https://fonts.googleapis.com/css2?family=Open+Sans:wght@600;700&display=swap" rel="stylesheet">
<style>
  :root {
    --sky: #33a6d7;
    --ocean: #3276b5;
    --slate: #3a4654;
    --white: #ffffff;
    --frame: #3a78b8;
    --bg-top: #0d5f61;
    --bg-mid: #6fb3a0;
    --bg-bottom: #c4f0d4;
    --swoosh: #4a4f55;
  }
  * { margin: 0; padding: 0; box-sizing: border-box; }
  html, body { width: 1200px; height: 1200px; overflow: hidden; }
  body {
    position: relative;
    background: linear-gradient(180deg, var(--bg-top) 0%, var(--bg-mid) 50%, var(--bg-bottom) 100%);
    font-family: "Open Sans", Arial, sans-serif;
  }
  .poster {
    position: absolute;
    width: 563px;
    height: 563px;
    background: var(--white);
    overflow: hidden;
  }
  .poster--plain { left: 29px; top: 29px; }
  .poster--band { left: 608px; top: 29px; }
  .poster--framed { left: 323px; top: 609px; border: 5px solid var(--frame); }

  .brand {
    position: absolute;
    left: 0; right: 0; top: 100px;
    display: flex; align-items: center; justify-content: center; gap: 22px;
  }
  .brand__dot {
    width: 78px; height: 78px; border-radius: 50%;
    background: var(--sky);
  }
  .brand__name {
    font-size: 74px; font-weight: 700; color: var(--slate);
    letter-spacing: -1px; line-height: 1;
  }

  .services {
    position: absolute; left: 0; right: 0; top: 244px;
    height: 180px;
  }
  .service {
    position: absolute; top: 0; width: 170px; text-align: center;
  }
  .service:nth-child(1) { left: 15px; }
  .service:nth-child(2) { left: 196px; }
  .service:nth-child(3) { left: 372px; }
  .service__art { position: relative; width: 170px; height: 140px; }
  .service__swoosh {
    position: absolute; left: 18px; top: 2px;
    width: 146px; height: 134px; border-radius: 50%;
    border-right: 5px solid var(--swoosh);
  }
  .service__photo {
    position: absolute; left: 10px; top: 4px;
    width: 144px; height: 132px; border-radius: 50%;
  }
  .service__photo--minding { background: radial-gradient(circle at 45% 55%, #b68a66 0%, #7c7a70 45%, #3f5a3a 100%); }
  .service__photo--visits { background: linear-gradient(180deg, #e6edf1 0%, #d8e4ea 40%, #4e8fb2 55%, #c79a62 78%, #b8875a 100%); }
  .service__photo--walking { background: radial-gradient(circle at 50% 45%, #e6d8c6 0%, #b8a88e 35%, #4d8a3e 75%, #2f5e2a 100%); }
  .service__label {
    margin-top: 12px;
    font-size: 18px; font-weight: 700; color: var(--ocean);
  }

  .contact {
    position: absolute; left: 0; right: 0; text-align: center;
  }
  .poster--plain .contact { top: 476px; }
  .contact__web { font-size: 23px; font-weight: 700; color: var(--sky); line-height: 1.2; }
  .contact__phone { font-size: 19px; font-weight: 700; color: var(--ocean); line-height: 1.3; }

  .contact--band {
    top: auto; bottom: 0; height: 112px;
    background: var(--sky);
    display: flex; flex-direction: column; justify-content: center;
  }
  .contact--band .contact__web,
  .contact--band .contact__phone { color: var(--white); }
</style>
</head>
<body>

  <section class="poster poster--plain">
    <div class="brand"><span class="brand__dot"></span><span class="brand__name">Paw Haven</span></div>
    <div class="services">
      <div class="service">
        <div class="service__art"><span class="service__swoosh"></span><div class="service__photo service__photo--minding" role="img" aria-label="Photo of a merle dog resting for dog minding"></div></div>
        <p class="service__label">Dog Minding</p>
      </div>
      <div class="service">
        <div class="service__art"><span class="service__swoosh"></span><div class="service__photo service__photo--visits" role="img" aria-label="Photo of a blonde dog sitting by the sea for home visits"></div></div>
        <p class="service__label">Home Visits</p>
      </div>
      <div class="service">
        <div class="service__art"><span class="service__swoosh"></span><div class="service__photo service__photo--walking" role="img" aria-label="Photo of a bulldog on a lead on grass for dog walking"></div></div>
        <p class="service__label">Dog Walking</p>
      </div>
    </div>
    <div class="contact">
      <p class="contact__web">www.pawhavenexample.com.au</p>
      <p class="contact__phone">Ph: 0491 570 156</p>
    </div>
  </section>

  <section class="poster poster--band">
    <div class="brand"><span class="brand__dot"></span><span class="brand__name">Paw Haven</span></div>
    <div class="services">
      <div class="service">
        <div class="service__art"><span class="service__swoosh"></span><div class="service__photo service__photo--minding" role="img" aria-label="Photo of a merle dog resting for dog minding"></div></div>
        <p class="service__label">Dog Minding</p>
      </div>
      <div class="service">
        <div class="service__art"><span class="service__swoosh"></span><div class="service__photo service__photo--visits" role="img" aria-label="Photo of a blonde dog sitting by the sea for home visits"></div></div>
        <p class="service__label">Home Visits</p>
      </div>
      <div class="service">
        <div class="service__art"><span class="service__swoosh"></span><div class="service__photo service__photo--walking" role="img" aria-label="Photo of a bulldog on a lead on grass for dog walking"></div></div>
        <p class="service__label">Dog Walking</p>
      </div>
    </div>
    <div class="contact contact--band">
      <p class="contact__web">www.pawhavenexample.com.au</p>
      <p class="contact__phone">Ph: 0491 570 156</p>
    </div>
  </section>

  <section class="poster poster--framed">
    <div class="brand"><span class="brand__dot"></span><span class="brand__name">Paw Haven</span></div>
    <div class="services">
      <div class="service">
        <div class="service__art"><span class="service__swoosh"></span><div class="service__photo service__photo--minding" role="img" aria-label="Photo of a merle dog resting for dog minding"></div></div>
        <p class="service__label">Dog Minding</p>
      </div>
      <div class="service">
        <div class="service__art"><span class="service__swoosh"></span><div class="service__photo service__photo--visits" role="img" aria-label="Photo of a blonde dog sitting by the sea for home visits"></div></div>
        <p class="service__label">Home Visits</p>
      </div>
      <div class="service">
        <div class="service__art"><span class="service__swoosh"></span><div class="service__photo service__photo--walking" role="img" aria-label="Photo of a bulldog on a lead on grass for dog walking"></div></div>
        <p class="service__label">Dog Walking</p>
      </div>
    </div>
    <div class="contact contact--band">
      <p class="contact__web">www.pawhavenexample.com.au</p>
      <p class="contact__phone">Ph: 0491 570 156</p>
    </div>
  </section>

</body>
</html>
```